Real Estate | Property Management Website Design

We are working with a Real Estate company in California. They provide Property Management Services and Real Estate Services.

PLEASE NOT: make sure the site covers real estate and property management).

A few websites for inspiration:
https://brimcastleleasing.example
https://www.harborvaleestates.example
https://morvenaltiski.example
https://tobelnashridge.example
https://theosterlundteam.example
https://brennaholtcamp.example
https://zvenhaus.example

Thank you for taking the time to consider designing a website for us. We are web developers based in Stockton, CA, USA. Most of our projects go through the same process. Understanding this process may help you win a project with us. We custom-code all of our websites in-house. We don’t have any requirements as to what tools you use for your design, but we ask that you follow these guidelines.

IMAGES:
If you use any images or icons in the design, we ask that you have a link to the asset so we can purchase the image/icon. Most of the designs we submit do not have the customer’s images on them unless they have some great images. Be creative; show us the feeling you are trying to portray with your image choices. Use any royalty-free site you choose. We subscribe to Quillory and mainly use their images, but we can purchase images outside of Quillory. PLEASE NOTE: we will not submit designs to clients with watermarks on the images.

FONTS:
We ask that you identify the fonts you’re using in the design. This can be done in a message if you want. We typically use Vantrel Fonts and Quillory Fonts.

CONTENT:
We're always open to different content and ideas. We often submit designs with stock images so the client can see our vision. We typically take pictures after the website launch to use their images with our vision. Lorem Ipsum is fine for paragraphs, but we ask that you make the Headers with correct English. We want to be able to show the vision and identify the sections of the website.

INSPIRATION:
We typically add a couple of links in the brief of websites we like to help you get started in your design.

REVISIONS:
We do not often ask for revisions of the designs unless we see something in the design that may not appeal to the client. If there are slight changes that we want to make, we do that in the development process.

FEEDBACK:
We rarely give feedback on designs during the design process. We are working on many website projects and do not have the time to provide feedback. We usually respond if your request is well thought out and asks specific questions, but a note asking “feedback, please” usually goes unanswered.

```html
<!DOCTYPE html>
<html lang="en">
<head>
<meta charset="utf-8">
<title>Larkmoor Estates</title>
<link href="https://fonts.googleapis.com/css2?family=Montserrat:ital,wght@0,400;0,500;0,600;0,700;1,400;1,500&display=swap" rel="stylesheet">
<style>
:root{
  --orange:#f86a25;
  --orange-dark:#df5818;
  --ink:#1a1a1a;
  --muted:#555;
  --light:#ebebeb;
  --mid:#dcdcdc;
  --card-active:#bdbdbd;
  --footer:#000;
  --footer-bar:#2b2b2b;
  --white:#fff;
}
*{margin:0;padding:0;box-sizing:border-box}
html,body{width:1200px;height:3572px;overflow:hidden}
body{font-family:"Montserrat",sans-serif;color:var(--ink);position:relative;background:var(--white)}
.abs{position:absolute}

/* header + hero */
.hero{left:0;top:0;width:1200px;height:686px;background:linear-gradient(180deg,#f4f5f7 0%,#b9c3cc 18%,#7f8a82 40%,#5c6f45 52%,#8a8c8e 62%,#6d6f71 100%)}
.brand{left:75px;top:22px;display:flex;align-items:center;gap:12px;font-size:26px;font-weight:700;color:var(--orange);letter-spacing:.5px}
.brand-mark{width:36px;height:36px;background:var(--orange)}
.nav{right:75px;top:26px;display:flex;gap:38px;font-size:14px}
.nav a{color:var(--ink);text-decoration:none}
.nav a.active{color:var(--orange)}

/* features */
.features{left:0;top:686px;width:1200px;height:148px;display:flex}
.feature{flex:1;display:flex;flex-direction:column;align-items:center;justify-content:center;gap:14px;color:var(--white);font-size:19px;font-weight:500}
.feature:nth-child(odd){background:var(--orange)}
.feature:nth-child(even){background:var(--orange-dark)}
.feature svg{width:52px;height:52px;stroke:#fff;fill:none;stroke-width:2}

/* about */
.about-img{left:0;top:834px;width:654px;height:652px}
.about-title{left:689px;top:934px;font-size:37px;font-weight:600;letter-spacing:1px}
.about-copy{left:689px;font-size:14px;line-height:18.7px;white-space:nowrap}
.btns{left:689px;top:1253px;display:flex;gap:45px}
.btn{background:var(--orange);color:#fff;width:143px;height:53px;display:flex;align-items:center;justify-content:center;font-size:15px}

/* agents */
.agents{left:0;top:1486px;width:1200px;height:734px;background:var(--light);text-align:center}
.kicker{position:absolute;top:76px;width:100%;font-style:italic;font-size:14px;color:#777}
.agents h2{position:absolute;top:110px;width:100%;font-size:38px;font-weight:700;color:var(--orange);letter-spacing:1px}
.agents .lead{position:absolute;top:182px;width:100%;font-size:14.5px;line-height:1.3}
.card{top:302px;width:247px;height:324px;background:var(--white);text-align:center}
.card.active{background:var(--card-active)}
.avatar{width:157px;height:157px;border-radius:50%;margin:37px auto 0}
.card h3{margin-top:44px;font-size:16px;font-style:italic;font-weight:500}
.card p{margin-top:16px;font-size:14px;color:var(--muted)}
.arrow{top:444px;width:24px;height:40px;stroke:#777;fill:none;stroke-width:3}

/* enquiry */
.enquiry{left:0;top:2220px;width:1200px;height:788px;background:var(--mid);text-align:center}
.enquiry h2{position:absolute;top:70px;width:100%;font-size:38px;font-weight:600}
.enquiry .lead{position:absolute;top:138px;width:100%;font-size:14.5px;line-height:1.5}
.enquiry h3{position:absolute;top:232px;width:100%;font-size:34px;font-weight:500;color:var(--orange)}
.enquiry .sub{position:absolute;top:287px;width:100%;font-size:14.5px}
.form{left:376px;top:325px;width:450px;height:382px;background:var(--white);text-align:left}
.form h4{position:absolute;left:36px;top:40px;font-size:23px;font-weight:500}
.field{position:absolute;border:1px solid #aaa;border-radius:3px;background:#f1f1f1;font-size:11px;padding:12px 13px;color:#222}
.submit{position:absolute;left:166px;top:298px;width:118px;height:40px;background:var(--orange);color:#fff;font-size:15px;display:flex;align-items:center;justify-content:center}

/* footer */
.footer{left:0;top:3008px;width:1200px;height:492px;background:var(--footer);color:var(--white)}
.footer h5{position:absolute;top:83px;font-size:23px;font-weight:500}
.footer .txt{position:absolute;font-size:12.5px;line-height:1.55}
.footer ul{position:absolute;list-style:none;font-size:12.5px;line-height:22px}
.socials{left:75px;top:264px;display:flex;gap:12px}
.socials span{width:40px;height:40px;border-radius:50%;background:var(--white)}
.socials span:nth-child(2){background:var(--orange)}
.sub-form{left:824px;top:208px;display:flex}
.sub-form .email{width:187px;height:60px;background:#fff;color:#999;font-size:16px;padding:20px 18px}
.sub-form .go{width:114px;height:60px;background:var(--orange);font-size:18px;display:flex;align-items:center;justify-content:center}
.copy{left:0;top:3500px;width:1200px;height:72px;background:var(--footer-bar);color:#fff;font-size:16px;display:flex;align-items:center;justify-content:center}
</style>
</head>
<body>

<div class="abs hero" role="img" aria-label="Modern office buildings beside a wide empty road with painted arrows"></div>
<div class="abs brand"><span class="brand-mark"></span>Larkmoor Estates</div>
<nav class="abs nav">
  <a class="active" href="#">Home</a><a href="#">About us</a><a href="#">Social</a><a href="#">Our Property</a><a href="#">Compny</a><a href="#">Services</a><a href="#">Contact</a>
</nav>

<section class="abs features">
  <div class="feature"><svg viewBox="0 0 52 52"><rect x="6" y="8" width="34" height="36"/><rect x="12" y="14" width="10" height="10"/><line x1="26" y1="16" x2="36" y2="16"/><line x1="26" y1="22" x2="36" y2="22"/><rect x="12" y="30" width="24" height="8"/><line x1="40" y1="14" x2="46" y2="14"/><line x1="46" y1="14" x2="46" y2="48"/><line x1="10" y1="48" x2="46" y2="48"/></svg>Plans</div>
  <div class="feature"><svg viewBox="0 0 52 52"><circle cx="26" cy="28" r="14"/><circle cx="26" cy="28" r="6"/><path d="M26 4v10M20 9l6-5 6 5"/></svg>Upgrades</div>
  <div class="feature"><svg viewBox="0 0 52 52"><path d="M26 24c-5-6-8-10-8-14a8 8 0 0 1 16 0c0 4-3 8-8 14z"/><circle cx="26" cy="10" r="3"/><path d="M4 24l12-4 10 4 10-4 12 4v22l-12-4-10 4-10-4-12 4z"/><line x1="16" y1="20" x2="16" y2="42"/><line x1="36" y1="20" x2="36" y2="42"/></svg>Locations</div>
  <div class="feature"><svg viewBox="0 0 52 52"><path d="M28 44H8V4h20l8 8v12"/><path d="M28 4v8h8"/><line x1="14" y1="20" x2="28" y2="20"/><line x1="14" y1="27" x2="26" y2="27"/><circle cx="38" cy="38" r="11"/><path d="M38 31v13M33 39l5 5 5-5"/></svg>Downloads File</div>
</section>

<div class="abs about-img" role="img" aria-label="City skyline with a tall tower, a bridge and a ferris wheel under blue sky" style="background:linear-gradient(180deg,#2f7fc4 0%,#8ab9e0 45%,#7b8e9e 62%,#3e5e3a 85%,#2b4424 100%);clip-path:polygon(0 0,654px 0,499px 652px,0 652px)"></div>
<h2 class="abs about-title">WHO WE ARE</h2>
<p class="abs about-copy" style="top:1003px">Lorem ipsum dolor sit amet, consectetur adipiscing elit,<br>sed do eiusmod tempor incididunt ut labore et dolore magna<br>aliqua. Ut enim ad minim veniam,</p>
<p class="abs about-copy" style="top:1087px">Lorem ipsum dolor sit amet, consectetur adipiscing elit,<br>sed do eiusmod tempor incididunt ut labore et dolore magna<br>aliqua. Ut enim ad minim veniam,Lorem ipsum dolor sit amet,<br>consectetur adipiscing elit, sed do eiusmod tempor<br>incididunt ut labore et dolore magna aliqua. Ut enim ad<br>minim veniam,</p>
<div class="abs btns"><span class="btn">About More</span><span class="btn">Learn More</span></div>

<section class="abs agents">
  <p class="kicker">People &nbsp;we Trusted</p>
  <h2>OUR AGENTS</h2>
  <p class="lead">Lorem ipsum dolor sit amet, consectetur adipiscing elit,<br>sed do eiusmod tempor incididunt ut labore et dolore magna<br>aliqua. Ut enim ad minim veniam,</p>
  <svg class="abs arrow" style="left:24px" viewBox="0 0 24 40"><path d="M20 4L4 20l16 16"/></svg>
  <svg class="abs arrow" style="left:1146px" viewBox="0 0 24 40"><path d="M4 4l16 16L4 36"/></svg>
  <div class="abs card" style="left:75px"><div class="avatar" role="img" aria-label="Portrait of agent Tov Brannick" style="background:linear-gradient(180deg,#8fc3c9,#2c3440)"></div><h3>Tov Brannick</h3><p>Real Estate Brokered</p></div>
  <div class="abs card active" style="left:342px"><div class="avatar" role="img" aria-label="Portrait of agent Lisa" style="background:linear-gradient(180deg,#8a7566,#2a2420)"></div><h3>Lisa</h3><p>Real Estate Brokered</p></div>
  <div class="abs card" style="left:611px"><div class="avatar" role="img" aria-label="Portrait of agent Corin" style="background:linear-gradient(180deg,#e4e4e4,#2c3a52)"></div><h3>Corin</h3><p>Real Estate Brokered</p></div>
  <div class="abs card" style="left:877px"><div class="avatar" role="img" aria-label="Portrait of agent Nadia" style="background:linear-gradient(180deg,#6c5a4c,#2e2a2a)"></div><h3>Nadia</h3><p>Real Estate Brokered</p></div>
</section>

<section class="abs enquiry">
  <h2>Enquiry Now!</h2>
  <p class="lead">Lorem ipsum dolor sit amet, consectetur adipiscing elit, sed do eiusmod tempor incididunt<br>ut labore et dolore magna aliqua. Ut enim ad minim veniam,</p>
  <h3>Sign up</h3>
  <p class="sub">Lorem ipsum dolor sit amet, consectetur adipiscing elit,</p>
  <div class="abs form">
    <h4>Ask a Questions</h4>
    <div class="field" style="left:22px;top:81px;width:192px;height:36px">First Name</div>
    <div class="field" style="left:234px;top:81px;width:192px;height:36px">Last Name</div>
    <div class="field" style="left:22px;top:137px;width:192px;height:36px">Email</div>
    <div class="field" style="left:234px;top:137px;width:192px;height:36px">Phone</div>
    <div class="field" style="left:22px;top:192px;width:404px;height:74px">Masage</div>
    <span class="submit">Submit</span>
  </div>
</section>

<footer class="abs footer">
  <h5 style="left:75px">About us</h5>
  <p class="txt" style="left:75px;top:150px;width:290px">Lorem ipsum dolor sit amet, consectetur adipiscing elit, sed do eiusmod tempor incididunt ut labore et dolore magna aliqua. Ut enim ad minim veniam,</p>
  <div class="abs socials"><span></span><span></span><span></span><span></span></div>
  <h5 style="left:416px">Quick Links</h5>
  <ul style="left:423px;top:150px"><li>Home</li><li>About us</li><li>Compny</li><li>Services</li><li>Contact</li></ul>
  <h5 style="left:607px">Information</h5>
  <ul style="left:607px;top:150px"><li>Privacy Policy</li><li>Terms</li><li>Contact</li></ul>
  <h5 style="left:819px">Newslatter</h5>
  <p class="txt" style="left:824px;top:150px;width:290px;line-height:1.8">Subscribe to our Newsletter for latest news and updates.</p>
  <div class="abs sub-form"><span class="email">Email</span><span class="go">Subscribe</span></div>
</footer>
<div class="abs copy">Copyright © 2023 | Privacy Policy</div>

</body>
</html>
```